PowerPoint Design Project for Retirement Planning Company

Please design a powerpoint presentation template for our retirement planning company called Pine Harbor Advisors. We need a cover page and slide pages in both portrait and landscape orientation. We make many presentations to clients.

Our tagline is "Retirement Planning. Simplified." We are educators in the retirement planning space. Our company educates small and mid-sized businesses in the board room and break room on how to select a retirement plan for the company and their employees that will help them retire ready. Our slide deck needs to have appeal to a CEO in the board room and a blue collar worker in the breakroom.

We are looking for a template that incorporates our logo, tagline images, colors - green, gray and brown (see uploaded files for examples). The design needs to be clean with plenty of space for text. It needs to be crisp, modern, and eye catching.

We look forward to seeing how you use the images in our business card and logo to achieve a pleasing design. You are the experts so we hope you will develop some innovative designs that wow us and give our clients the confidence that we are experts and put together.
Updates

Designers - Thanks for your great work so far.  

Please do not include the website address on the powerpoint template.

Please provide one template per submission.  When they are grouped together, it is too hard to see the details on your slides.  

Thanks!

Target Market(s)

CEOs and Executive teams at small to medium sized businesses that care about their employees future retirement

Industry/Entity Type

Landscape

Requirements
Must have
• 1) Cover Page (should double as a report cover as well)

2) Second Page for text

3) Third Page for illustrations/graphs/charts

Landscape orientation and Portrait orientation

Colors:

Brown light : C=35, M=60, Y=80, K=25
Brown dark : C=40, M=70, Y=100, K=50

Gray Icon Border: C=0, M=0, Y=0, K=80
Gray Icon Background: C=0, M=0, Y=0, K=5
Gray Letters: C=0, M=0, Y=0, K=80
Gray Light Person: C=0, M=0, Y=0, K=40
Gray Dark Person: C=0, M=0, Y=0, K=60
Gray Dark Wheel Checked: C=0, M=0, Y=0, K=90

Green Light 1: C=40, M=8, Y=85, K=0
Green Light 2: C=53, M=17, Y=100, K=0
Green Dark: C=67, M=39, Y=100, K=27

White: C=0, M=0, Y=0, K=0

Black: C=0, M=0, Y=0, K=100

Fonts:
Logo and graphics files
Footlight MT Light
BrowalliaUPC

Business card/Letterhead files
Calisto MT
Segoe UI

Nice to have
• Please look at the back of our business card design. It has a version of our logo in an abstract form. Consider this concept in full color or a grayed out version as a backdrop.

Use of the "hill" with our tagline is another concept that could be incorporated into the design. See front of our business card and letterhead.

I have uploaded a diagram (wheel diagram full color) that we use to describe our services, plus all the images we use to describe our services (pdf). These images needs to look good as content on a slide.

```html
<!DOCTYPE html>
<html lang="en">
<head>
<meta charset="utf-8">
<title>Pine Harbor Advisors – Cover</title>
<link rel="stylesheet" href="https://fonts.googleapis.com/css2?family=Roboto+Condensed:wght@700&family=Open+Sans:wght@400&family=Cinzel:wght@400&display=swap">
<style>
  :root {
    --green-deep: #26361a;
    --green-mid: #3b5426;
    --green-glow: #4f6d33;
    --green-logo: #3f5a22;
    --white: #ffffff;
    --title-shadow: rgba(0, 0, 0, 0.35);
  }
  html, body {
    margin: 0;
    padding: 0;
    width: 1200px;
    height: 900px;
    overflow: hidden;
    background: var(--green-deep);
  }
  .cover {
    position: relative;
    width: 1200px;
    height: 900px;
    overflow: hidden;
    background:
      radial-gradient(ellipse 70% 75% at 62% 48%, var(--green-glow) 0%, var(--green-mid) 45%, var(--green-deep) 100%);
  }
  .brand-backdrop {
    position: absolute;
    left: 0;
    top: 0;
    width: 1200px;
    height: 900px;
  }
  .brand-badge {
    position: absolute;
    left: 585px;
    top: -395px;
    width: 600px;
    height: 600px;
    border-radius: 50%;
    background: var(--white);
  }
  .brand-name {
    position: absolute;
    left: 628px;
    top: 44px;
    display: flex;
    align-items: center;
    gap: 14px;
    color: var(--green-logo);
    font-family: "Cinzel", Georgia, serif;
    font-weight: 400;
    font-size: 30px;
    letter-spacing: 1px;
    white-space: nowrap;
  }
  .brand-dot {
    width: 56px;
    height: 56px;
    border-radius: 50%;
    background: var(--green-logo);
    flex: none;
  }
  .cover-title {
    position: absolute;
    right: 40px;
    top: 474px;
    margin: 0;
    color: var(--white);
    font-family: "Roboto Condensed", "Arial Narrow", sans-serif;
    font-weight: 700;
    font-size: 73px;
    line-height: 1;
    text-shadow: 0 3px 6px var(--title-shadow);
    white-space: nowrap;
  }
  .cover-tagline {
    position: absolute;
    right: 52px;
    top: 834px;
    margin: 0;
    color: var(--white);
    font-family: "Open Sans", "Segoe UI", sans-serif;
    font-weight: 400;
    font-size: 36px;
    line-height: 1;
    white-space: nowrap;
  }
</style>
</head>
<body>
  <main class="cover">
    <svg class="brand-backdrop" viewBox="0 0 1200 900" role="img" aria-label="Faint abstract brand backdrop in deep green">
      <defs>
        <radialGradient id="backdropFill" cx="0.45" cy="0.45" r="0.6">
          <stop offset="0" stop-color="#2f4420" stop-opacity="0.9"/>
          <stop offset="1" stop-color="#1f2e15" stop-opacity="0.7"/>
        </radialGradient>
      </defs>
      <circle cx="265" cy="455" r="415" fill="url(#backdropFill)"/>
    </svg>

    <div class="brand-badge"></div>
    <div class="brand-name">
      <span class="brand-dot"></span>
      <span>Pine Harbor Advisors</span>
    </div>

    <h1 class="cover-title">Presentation Title Here</h1>
    <p class="cover-tagline">Retirement Plans. Made Clear.</p>
  </main>
</body>
</html>
```